Book Cover Design Project

We need a book cover for a eBook on internet banking.

This eBook is meant to be an easy to read, practical book to help people understand what internet banking is, the pros and cons and cover the pure 'internet only' banks that have no branches. The intention is to help people to make informed decisions about whether to use internet banking, how to use it safely and explain in detail what 'internet only' banks are and whether they are right for them.

The cover should not look technical so that non-technical people are not scared off by the look. I have uploaded a book cover design that has the style that I am trying to portray, I have also uploaded a front cover that I created but do not think is suitable.

The cover wording layout could be something like
"Internet Banking"
"A practical guide to answer all your questions" or "The ultimate guide to internet banking" or "The Who's What's and How's of Internet Banking"
Authors name : Clive Mortlock

Industry/Entity Type

Internet

```html
<!DOCTYPE html>
<html lang="en">
<head>
<meta charset="utf-8">
<title>Internet Banking — Clive Mortlock</title>
<link rel="stylesheet" href="https://fonts.googleapis.com/css2?family=Oswald:wght@700&family=Roboto+Condensed:wght@700&family=Roboto:wght@700&display=swap">
<style>
  :root {
    --ink: #000000;
    --white: #ffffff;
    --gold-deep: #a8732a;
    --gold-mid: #d7a24b;
    --gold-light: #f6dc86;
    --ray-light: #dcdcdc;
    --ray-mid: #8a8a8a;
    --ray-dark: #2a2a2a;
    --cash-cream: #e9e2cc;
    --skin-warm: #d9a77c;
  }
  html, body {
    margin: 0;
    padding: 0;
    width: 795px;
    height: 1200px;
    overflow: hidden;
    background: var(--ink);
  }
  .cover {
    position: relative;
    width: 795px;
    height: 1200px;
    background: var(--ink);
    overflow: hidden;
  }
  .cover__title {
    position: absolute;
    left: 0;
    top: 0;
    width: 795px;
    height: 320px;
  }
  .cover__title text {
    font-family: "Oswald", "Arial Narrow", sans-serif;
    font-weight: 700;
  }
  .cover__subtitle {
    position: absolute;
    left: 0;
    top: 346px;
    width: 795px;
    text-align: center;
    font-family: "Roboto Condensed", "Arial Narrow", sans-serif;
    font-weight: 700;
    font-size: 38px;
    line-height: 1;
    letter-spacing: 1px;
    color: var(--gold-mid);
    margin: 0;
  }
  .cover__rule-top {
    position: absolute;
    left: 0;
    top: 421px;
    width: 795px;
    height: 10px;
    background: linear-gradient(90deg, var(--gold-deep), var(--gold-light) 45%, var(--gold-mid) 75%, var(--gold-deep));
  }
  .cover__artwork {
    position: absolute;
    left: 0;
    top: 431px;
    width: 795px;
    height: 523px;
    background:
      linear-gradient(180deg, rgba(0,0,0,0) 0%, rgba(0,0,0,0) 78%, var(--ink) 96%),
      radial-gradient(ellipse 22% 40% at 50% 48%, var(--cash-cream) 0%, var(--skin-warm) 45%, rgba(217,167,124,0) 100%),
      radial-gradient(ellipse 75% 85% at 50% 82%, #f2f2f2 0%, var(--ray-light) 20%, var(--ray-mid) 50%, var(--ray-dark) 80%, #111111 100%);
  }
  .cover__author {
    position: absolute;
    left: 0;
    top: 1078px;
    width: 795px;
    text-align: center;
    font-family: "Roboto", Arial, sans-serif;
    font-weight: 700;
    font-size: 52px;
    line-height: 1;
    letter-spacing: 1px;
    margin: 0;
    color: var(--gold-mid);
    background: linear-gradient(180deg, var(--gold-light), var(--gold-deep));
    -webkit-background-clip: text;
    background-clip: text;
    -webkit-text-fill-color: transparent;
  }
  .cover__rule-bottom {
    position: absolute;
    left: 0;
    top: 1166px;
    width: 795px;
    height: 14px;
    background: linear-gradient(90deg, rgba(168,115,42,0.1), var(--gold-mid) 40%, var(--gold-light) 80%, var(--gold-mid));
  }
</style>
</head>
<body>
  <main class="cover">
    <svg class="cover__title" viewBox="0 0 795 320" aria-labelledby="book-title">
      <title id="book-title">Internet Banking</title>
      <defs>
        <linearGradient id="title-gold" x1="0" y1="0" x2="1" y2="0">
          <stop offset="0" stop-color="#a8732a"/>
          <stop offset="0.45" stop-color="#f6dc86"/>
          <stop offset="0.75" stop-color="#d7a24b"/>
          <stop offset="1" stop-color="#a8732a"/>
        </linearGradient>
      </defs>
      <text x="90" y="146" font-size="116" textLength="645" lengthAdjust="spacingAndGlyphs" fill="url(#title-gold)">INTERNET</text>
      <text x="99" y="307" font-size="175" textLength="636" lengthAdjust="spacingAndGlyphs" fill="var(--white)">BANKING</text>
    </svg>

    <p class="cover__subtitle">The ultimate guide to internet banking</p>

    <div class="cover__rule-top"></div>

    <div class="cover__artwork" role="img" aria-label="Photo of a raised fist clutching crumpled dollar bills, rising from a black city skyline silhouette against grey and white sunburst rays"></div>

    <p class="cover__author">CLIVE MORTLOCK</p>

    <div class="cover__rule-bottom"></div>
  </main>
</body>
</html>
```